New Business card design to reflect rebrand

I would like a business card design with a good base colour for our new logo and also a placeholder for a profile pic of the card holder. the design needs to be editable to the point that we can easily change the picture of the person and use that design for printmoor etc. we are looking at a metalic finish business card so will need a good base colour to bring out the finish.

Target Market(s)

prospective customers

Industry/Entity Type

Business

Contact Information for Business Card

I would like one editable design that we can change the name of the card holder and profile picture. The design need to be in a format that be send to printmoor etc.

Our address is Fenwick Lodge, Mill Lane, Ashcombe Green, RG41 3TQ Tel no. 01632 960417

Requirements
Must have
• place holder for a profile pic for the card holder. in AI or preferably PSD format

```html
<!DOCTYPE html>
<html lang="en">
<head>
<meta charset="utf-8">
<title>Corvane Workplace Services – Business Card</title>
<link rel="stylesheet" href="https://fonts.googleapis.com/css2?family=Didact+Gothic&family=Open+Sans:wght@400;600&display=swap">
<style>
  :root {
    --bg: #3a3532;
    --card-black: #0c0c0d;
    --band: #17181e;
    --slate: #5a7290;
    --orange: #f26a1b;
    --text-light: #e9e9ea;
    --photo-top: #4a4d58;
    --photo-bottom: #1d1f2c;
  }
  * { margin: 0; padding: 0; box-sizing: border-box; }
  html, body { width: 1200px; height: 900px; overflow: hidden; }
  body {
    background: var(--bg);
    font-family: "Open Sans", Arial, sans-serif;
    position: relative;
  }
  .card {
    position: absolute;
    width: 540px;
    height: 310px;
    background: var(--card-black);
    overflow: hidden;
    border-radius: 4px;
    box-shadow: 0 10px 30px rgba(0,0,0,0.45);
  }
  .card-front { left: 50px; top: 300px; }
  .card-back  { left: 620px; top: 300px; }

  /* Front */
  .front-band {
    position: absolute;
    left: 0; right: 0; bottom: 0;
    height: 150px;
    background: var(--band);
  }
  .portrait-slot {
    position: absolute;
    left: 30px; bottom: 0;
    width: 230px; height: 230px;
    background: linear-gradient(180deg, var(--photo-top), var(--photo-bottom));
    border-radius: 115px 115px 0 0;
  }
  .holder-name {
    position: absolute;
    left: 250px; top: 46px;
    font-family: "Didact Gothic", "Century Gothic", sans-serif;
    font-size: 17px;
    letter-spacing: 1.5px;
    color: var(--slate);
    text-transform: uppercase;
  }
  .holder-name .surname { color: var(--orange); }
  .contact-list {
    position: absolute;
    left: 250px; top: 80px;
    list-style: none;
    font-size: 11.5px;
    line-height: 17px;
    color: var(--text-light);
  }
  .contact-list li { display: flex; align-items: center; gap: 6px; }
  .contact-list .icon { width: 10px; height: 10px; fill: var(--slate); }
  .contact-list .address { padding-left: 16px; }
  .front-brand {
    position: absolute;
    right: 40px; bottom: 50px;
    font-family: "Didact Gothic", "Century Gothic", sans-serif;
    font-size: 46px;
    letter-spacing: 3px;
    color: var(--slate);
    text-transform: uppercase;
  }

  /* Back */
  .back-brand {
    position: absolute;
    left: 0; right: 0; top: 120px;
    text-align: center;
    font-family: "Didact Gothic", "Century Gothic", sans-serif;
    font-size: 30px;
    letter-spacing: 3px;
    line-height: 36px;
    color: var(--slate);
    text-transform: uppercase;
  }
</style>
</head>
<body>
  <section class="card card-front">
    <div class="front-band"></div>
    <div class="portrait-slot" role="img" aria-label="Profile photo of the card holder"></div>
    <h1 class="holder-name">Oliver <span class="surname">Brennan</span></h1>
    <ul class="contact-list">
      <li>
        <svg class="icon" viewBox="0 0 10 10" aria-hidden="true"><path d="M2 0.5 L3.6 2.6 L2.8 3.6 Q4 6 6.4 7.2 L7.4 6.4 L9.5 8 L8.3 9.5 Q3.5 9 0.5 1.7 Z"/></svg>
        01632 960417
      </li>
      <li>
        <svg class="icon" viewBox="0 0 10 10" aria-hidden="true"><path d="M0.5 2 H9.5 V8.5 H0.5 Z M0.5 2 L5 5.5 L9.5 2" stroke="#0c0c0d" stroke-width="0.8"/></svg>
        info@corvane.com
      </li>
      <li class="address">Fenwick Lodge, Mill Lane,</li>
      <li class="address">Ashcombe Green, RG41 3TQ</li>
    </ul>
    <div class="front-brand">Corvane</div>
  </section>

  <section class="card card-back">
    <div class="back-brand">Corvane<br>Workplace Services</div>
  </section>
</body>
</html>
```